Corporate flyer introducing a brand new technology apprenticeship program in Australia!

A professional, yet clean and contemporary looking flyer to advertise a brand new service offering in a simple, easy to read format with engaging images. Here is a link to our current online brochure which outlines the program we would like to advertise in a hardcopy flyer/brochure format: https://pages.vendrap.com/Information-on-Technology-Higher-Apprenticeships-for-Employers-Victoria-kT3pzqW7LmRe

Target Market(s)

Medium to large sized businesses involved in using cutting edge technology, such as engineering and advanced manufracturing (3D printing etc)

Industry/Entity Type

Engineering

Colors

Designer to choose colors to be used in the design.

Requirements
Must have
• Contemporary, clean looking, easy to read, tech/engineering/advanced manufacturing related imagery
Nice to have
• Some ideas about different sizes/styles (eg something other than a plain A4 sheet)
Should not have
• Unprofessional or offensive language

```html
<!DOCTYPE html>
<html lang="en">
<head>
<meta charset="utf-8">
<title>Technology Higher Apprentices Program</title>
<link href="https://fonts.googleapis.com/css2?family=Nunito+Sans:wght@400;600;700;800&display=swap" rel="stylesheet">
<style>
  :root {
    --navy: #2e3446;
    --red: #e5301d;
    --ink: #3a3d45;
    --paper: #ffffff;
    --page: #ececec;
    --soft: #f3f3f4;
  }
  * { margin: 0; padding: 0; box-sizing: border-box; }
  html, body { width: 1200px; height: 836px; overflow: hidden; }
  body { background: var(--page); font-family: "Nunito Sans", Arial, sans-serif; color: var(--ink); }

  .flyer { position: absolute; left: 310px; top: 13px; width: 580px; height: 810px; background: var(--paper); overflow: hidden; }
  .flyer-wash { position: absolute; left: 0; top: 290px; width: 580px; height: 520px; }

  .brand { position: absolute; left: 50px; top: 52px; display: flex; align-items: center; gap: 10px; }
  .brand-mark { width: 14px; height: 14px; background: var(--navy); }
  .brand-name { font-weight: 800; font-size: 22px; color: var(--navy); line-height: 1; }

  .hero-band { position: absolute; left: 0; top: 115px; width: 580px; height: 176px; background: var(--navy); }
  .hero-photo { position: absolute; left: 0; top: 0; }
  .hero-title { position: absolute; left: 38px; top: 146px; color: #fff; font-weight: 800; font-size: 27px; line-height: 28px; }
  .hero-sub { position: absolute; left: 40px; top: 216px; color: #fff; font-weight: 700; font-size: 12.2px; line-height: 16px; }

  .photo { position: absolute; }
  .photo-engineer { left: 40px; top: 270px; width: 248px; height: 161px; background: linear-gradient(135deg, #5f6e78, #2c3942 60%, #1d262d); }
  .photo-meeting { left: 312px; top: 502px; width: 248px; height: 150px; background: linear-gradient(160deg, #6f8f3d, #c9b89a 45%, #3c5a2a); }

  .section-bar { position: absolute; height: 36px; background: var(--navy); display: flex; align-items: center; color: #fff; font-weight: 800; font-size: 10.6px; text-transform: uppercase; line-height: 11px; }
  .section-bar .icon { width: 36px; height: 36px; background: var(--red); display: flex; align-items: center; justify-content: center; margin-right: 10px; flex: none; }

  .bar-about { left: 40px; top: 431px; width: 248px; }
  .bar-pilot { left: 40px; top: 628px; width: 248px; }
  .bar-industry { left: 312px; top: 270px; width: 248px; }
  .bar-course { left: 312px; top: 366px; width: 248px; }
  .bar-forward { left: 312px; top: 652px; width: 248px; }

  .copy { position: absolute; font-size: 8px; line-height: 9.8px; color: var(--ink); }
  .copy p + p { margin-top: 5px; }
  .copy-about { left: 40px; top: 476px; width: 248px; }
  .copy-pilot { left: 40px; top: 672px; width: 248px; }
  .copy-industry { left: 312px; top: 311px; width: 248px; }
  .copy-course { left: 312px; top: 407px; width: 248px; }
  .copy-forward { left: 312px; top: 694px; width: 248px; }

  .contact { position: absolute; left: 312px; top: 734px; list-style: none; }
  .contact li { display: flex; align-items: center; gap: 14px; font-size: 8.4px; font-weight: 800; color: var(--navy); height: 20px; }
  .contact svg { width: 12px; height: 12px; flex: none; }
</style>
</head>
<body>
<main class="flyer">
  <svg class="flyer-wash" viewBox="0 0 580 520" aria-hidden="true">
    <polygon points="0,80 260,0 320,520 0,520" fill="var(--soft)"/>
    <polygon points="300,160 580,60 580,400" fill="var(--soft)"/>
  </svg>

  <div class="brand">
    <span class="brand-mark"></span>
    <span class="brand-name">Nexa Group</span>
  </div>

  <div class="hero-band"></div>
  <svg class="hero-photo" width="580" height="290" viewBox="0 0 580 290">
    <defs>
      <linearGradient id="heroTone" x1="0" y1="0" x2="1" y2="1">
        <stop offset="0" stop-color="#3b3f4c"/>
        <stop offset=".55" stop-color="#c4260f"/>
        <stop offset="1" stop-color="#e5301d"/>
      </linearGradient>
    </defs>
    <polygon points="318,0 356,0 420,250 380,250" fill="#e2e2e4"/>
    <polygon points="318,0 580,0 580,250 380,250" fill="url(#heroTone)" role="img" aria-label="Photo of two colleagues talking at a meeting table, red toned"/>
    <polygon points="500,0 580,0 580,70" fill="var(--red)"/>
    <polygon points="565,22 580,22 580,45" fill="#fff"/>
  </svg>

  <h1 class="hero-title">Technology Higher<br>Apprentices Program</h1>
  <p class="hero-sub">Join Industry Leaders In This Unique Program Aimed<br>At Future Proofing Australian Businesses.</p>

  <div class="photo photo-engineer" role="img" aria-label="Photo of an engineer in a hard hat and hi-vis vest with technical overlay graphics"></div>

  <div class="section-bar bar-about">
    <span class="icon"><svg width="18" height="14" viewBox="0 0 18 14"><path d="M1 1h6a2 2 0 0 1 2 2v10a2 2 0 0 0-2-2H1zM17 1h-6a2 2 0 0 0-2 2v10a2 2 0 0 1 2-2h6z" fill="#fff"/></svg></span>About
  </div>
  <div class="copy copy-about">
    <p>The Technology Higher Apprenticeships combine the best of Higher Education and Vocational learning models by training future technicians to a higher skill and knowledge level to meet the needs of an Industry 4.0 based economy.</p>
    <p>These Higher Apprentices are employed in a model similar to a traditional paid apprenticeship while they are also enrolled in a Diploma of Applied Technologies, followed by an Associate Degree covering a range of topics related to emerging technology. The Higher Apprentices will also complete a number of intensive projects where they will commission a cyber-physical system to provide a solution or enhancement for your business. During these projects, the Higher Apprentices will have access to Kelvale's world-class Factory of the Future.</p>
  </div>

  <div class="section-bar bar-pilot">
    <span class="icon"><svg width="20" height="14" viewBox="0 0 20 14"><path d="M10 1 19 5 10 9 1 5z M5 7v4c3 2 7 2 10 0V7l-5 2z" fill="#fff"/></svg></span>Industry 4.0 Higher<br>Apprenticeships Pilot Program
  </div>
  <div class="copy copy-pilot">
    <p>The program utilises an apprenticeship framework to deliver a new Diploma and Associate Degree in Applied Technologies.</p>
    <p>The original project is funded as a pilot by the Arvena Skills Council, led and managed by the Nexa Group, and implemented in collaboration with Voltrix and Kelvale University of Technology.</p>
    <p>Focusing on Industry 4.0 and the Internet of Things, IT Disruptive Technologies, Engineering, Design and Business, the course will enable employers to train future technicians with a higher skills level to meet their needs in an Industry 4.0 based economy.</p>
  </div>

  <div class="section-bar bar-industry">
    <span class="icon"><svg width="18" height="16" viewBox="0 0 18 16"><path d="M1 15V7l4 2V5l4 2V3l4 2V1h4v14z" fill="#fff"/></svg></span>What is Industry 4.0
  </div>
  <div class="copy copy-industry">
    <p>The term Industry 4.0 encompasses the digitalisation of production processes based on devices autonomously communicating with each other along a value chain. Production units become 'smart factories' where computer-driven systems monitor physical processes.</p>
  </div>

  <div class="section-bar bar-course">
    <span class="icon"><svg width="18" height="18" viewBox="0 0 18 18"><circle cx="9" cy="9" r="6" fill="none" stroke="#fff" stroke-width="2.4" stroke-dasharray="3 2"/><circle cx="9" cy="9" r="2.5" fill="#fff"/></svg></span>Course Structure
  </div>
  <div class="copy copy-course">
    <p>The Program currently has a 4-year delivery timeline. Nexa Group envisages working with each company hosting a Technology Higher Apprentice, as well as with the relevant training provider on appropriate attendance schedules that maximise benefits for students, and the workplace. Training will be conducted in the work place, as well as the off-the-job delivery at the relevant training provider's facilities.</p>
  </div>

  <div class="photo photo-meeting" role="img" aria-label="Photo of people working together around a laptop at an outdoor table"></div>

  <div class="section-bar bar-forward">
    <span class="icon"><svg width="18" height="16" viewBox="0 0 18 16"><path d="M1 15V7l4 2V5l4 2V3l4 2V1h4v14z" fill="#fff"/></svg></span>Let's Move Forward
  </div>
  <div class="copy copy-forward">
    <p>The future is determined by the decisions you make today. Lay a strong foundation for the future success of your business by talking to us about Higher Apprenticeships today.</p>
  </div>

  <ul class="contact">
    <li><svg viewBox="0 0 12 12"><rect x="1" y="2.5" width="10" height="7" fill="none" stroke="var(--red)" stroke-width="1.4"/><path d="M1 3l5 3.5L11 3" fill="none" stroke="var(--red)" stroke-width="1.4"/></svg>talent@nexagroup.com.au</li>
    <li><svg viewBox="0 0 12 12"><path d="M3 1l2 3-1.3 1.3a7 7 0 0 0 3 3L8 7l3 2-1.5 2C5 11 1 7 1 2.5z" fill="var(--red)"/></svg>1300 555 019</li>
    <li><svg viewBox="0 0 12 12"><circle cx="6" cy="6" r="5" fill="none" stroke="var(--red)" stroke-width="1.2"/><ellipse cx="6" cy="6" rx="2.2" ry="5" fill="none" stroke="var(--red)" stroke-width="1"/><path d="M1 6h10" stroke="var(--red)" stroke-width="1"/></svg>nexagroup.com.au</li>
  </ul>
</main>
</body>
</html>
```